Flyer Design Project

We are a start-up real estate brokerage looking to attract new agents. Our business relies heavily on technology to help give agents more time to spend with clients. Our model is also different from a typical broker in that we do not take a percentage of commission from each sale an agent makes. Instead we charge a simple flat monthly fee and the agent keeps 100% of the commission the earn.
The ideal flyer will be pleasing to the eye, should probably have some appropriate graphics, use our logo and project a modern yet sophisticated company image. This is and advertising flyer that will be followed up with a more detailed brochure (later project).
Updates

While I like the initial design I was looking for more of a change from my design.  Here are some clarifications:

The design should not included the "click" option so it can be used online or in print.  Instead include the site corvelliahomes.com/careers

I want more of a list of features with less description.  The list should have:
- Deal Tracker included
- No Commission Split
- No Floor Time... Leads sent directly to you
- E & O Insurance included
- All your listings showcased on Homefinda.com
- Showing appointment solution.

Some description of each can be included but less of a question answer style than what I originally had.
It does not need to be a straight list, the items all need to be mentioned somewhere on the flyer but not necessarily in a list style.
Maybe an image of business meeting or greeting (agent joining).

Please do not hesitate to ask questions for clarification

The image of meeting or greeting is optional - you choose what you think is best.
Also, use of the "About Us" that was uploaded my be a good idea.  - I'm not sure on this either

Target Market(s)

current real estate agents and people considering a real estate career

Industry/Entity Type

Real Estate

Requirements
Must have
• Should list that we include "Deal Tracker" which is considered the top program for real estate agents (info and logos can be found at dealtracker.com)
Should highlight our low cost structure ($350 per month) and no transaction fees.
Should highlight that no office time is required. We provide virtual office solutions to save time.
Our contact number (555) 482-9167 ext. 204
Nice to have
• Any other additional information from the attached flyers (which should not be used as a template as they all need to be designed in a later project).

```html
<!DOCTYPE html>
<html lang="en">
<head>
<meta charset="utf-8">
<title>Corvellia Homes – Join Our Team</title>
<link href="https://fonts.googleapis.com/css2?family=EB+Garamond:wght@400;500;600;700&display=swap" rel="stylesheet">
<style>
  :root {
    --page-bg: #e8e8e8;
    --header-black: #000000;
    --logo-green: #0f2620;
    --band-grey: #b2b2b3;
    --circle-grey: #b6b6b7;
    --brand-red: #9e1a31;
    --ball-red: #a3182f;
    --white: #ffffff;
    --ink: #111111;
  }
  * { margin: 0; padding: 0; box-sizing: border-box; }
  html, body { width: 962px; height: 1200px; overflow: hidden; }
  body {
    position: relative;
    background: var(--page-bg);
    font-family: "EB Garamond", Georgia, serif;
  }
  .flyer {
    position: absolute;
    left: 59px; top: 87px;
    width: 816px; height: 1055px;
    background: var(--white);
    overflow: hidden;
  }
  .header {
    position: absolute; left: 0; top: 0;
    width: 816px; height: 191px;
    background: var(--header-black);
  }
  .brand-plate {
    position: absolute; left: 121px; top: 37px;
    width: 554px; height: 138px;
    background: var(--logo-green);
    display: flex; align-items: center; justify-content: center;
  }
  .brand-name {
    color: var(--white);
    font-weight: 500;
    font-size: 52px;
    letter-spacing: 2px;
    text-transform: uppercase;
    white-space: nowrap;
    text-align: center;
  }
  .about {
    position: absolute; left: 0; top: 191px;
    width: 816px; height: 193px;
    background: linear-gradient(180deg, #a9a9aa 0%, var(--band-grey) 60%);
  }
  .about-title {
    position: absolute; left: 62px; top: 81px;
    font-size: 21px; font-weight: 600;
    color: var(--ink); letter-spacing: 0.5px;
  }
  .about-text {
    position: absolute; left: 267px; top: 44px;
    width: 478px;
    font-size: 12.4px; line-height: 16px;
    color: var(--white); font-weight: 500;
    text-align: justify;
    hyphens: auto;
  }
  .photo {
    position: absolute; left: 0; top: 384px;
    width: 816px; height: 524px;
    background:
      radial-gradient(ellipse 45% 60% at 78% 65%, rgba(150,150,150,0.55) 0%, rgba(150,150,150,0) 100%),
      radial-gradient(ellipse 30% 55% at 38% 70%, rgba(60,75,100,0.45) 0%, rgba(60,75,100,0) 100%),
      radial-gradient(ellipse 15% 50% at 6% 75%, rgba(150,120,80,0.5) 0%, rgba(150,120,80,0) 100%),
      linear-gradient(180deg, #eef3f7 0%, #f4f6f8 40%, #d9dde2 100%);
  }
  .benefits-badge {
    position: absolute; left: 386px; top: 398px;
    width: 136px; height: 136px; border-radius: 50%;
    background: var(--circle-grey);
    box-shadow: 2px 4px 6px rgba(0,0,0,0.3);
    display: flex; align-items: center; justify-content: center;
    color: var(--white); font-size: 24px; font-weight: 600;
  }
  .benefit {
    position: absolute; height: 30px;
    background: rgba(255,255,255,0.9);
    color: var(--brand-red);
    font-size: 17px; font-weight: 700;
    text-transform: uppercase;
    display: flex; align-items: center;
    white-space: nowrap;
    box-shadow: 1px 2px 3px rgba(0,0,0,0.15);
  }
  .benefit.left { border-radius: 0 15px 15px 0; }
  .benefit.right { border-radius: 15px 0 0 15px; }
  .benefit.compact { font-size: 16px; }
  .tick-ball { position: absolute; width: 54px; height: 40px; }
  .price-badge {
    position: absolute; left: 72px; top: 768px;
    width: 176px; height: 176px; border-radius: 50%;
    background: var(--ball-red);
    box-shadow: 3px 4px 8px rgba(0,0,0,0.35);
    color: var(--white); text-transform: uppercase;
  }
  .price-badge span { position: absolute; white-space: nowrap; font-weight: 600; }
  .price-label { left: 24px; top: 25px; font-size: 11px; }
  .price-amount { left: 30px; top: 38px; font-size: 42px; line-height: 1; }
  .price-period { left: 48px; top: 78px; font-size: 17px; }
  .price-no { left: 80px; top: 96px; font-size: 40px; line-height: 1; }
  .price-fees { left: 36px; top: 135px; font-size: 10.5px; }
  .call {
    position: absolute; left: 171px; top: 957px;
    display: flex; align-items: center; gap: 12px;
    color: var(--brand-red); font-size: 26px; font-weight: 600;
    white-space: nowrap;
  }
</style>
</head>
<body>
  <main class="flyer">
    <header class="header">
      <div class="brand-plate"><span class="brand-name">Corvellia Homes</span></div>
    </header>

    <section class="about">
      <h2 class="about-title">ABOUT US</h2>
      <p class="about-text">Corvellia Homes is a boutique real estate firm specializing in residential properties on Long Island. Here at Corvellia Homes we focus on providing the personalized customer service associated with a traditional brick and mortar real estate firms while employing the latest technology to efficiently and effectively represent our clients at the lowest possible cost. With over 90% of home buyers searching online we saw a need to update the traditional brokerage model with a better balance of technology and service. Our company is founded on the belief that the use of technology can actually increase the quality of customer service in the real estate business.</p>
    </section>

    <div class="photo" role="img" aria-label="Photo of two businessmen shaking hands in a bright office, colleagues in the background"></div>

    <div class="benefits-badge">BENEFITS</div>

    <div class="benefit left" style="left:0;top:629px;width:349px;padding-left:109px;">Deal Tracker included</div>
    <div class="benefit left" style="left:0;top:675px;width:581px;padding-left:150px;">No floor time... leads sent directly to you</div>
    <div class="benefit left" style="left:0;top:722px;width:381px;padding-left:166px;">No commission split</div>
    <div class="benefit right" style="left:359px;top:770px;width:457px;padding-left:26px;">E &amp; O insurance included</div>
    <div class="benefit right compact" style="left:268px;top:819px;width:548px;padding-left:20px;">All your listings showcased on Homefinda.com</div>
    <div class="benefit right" style="left:304px;top:863px;width:512px;padding-left:39px;">Showing appointment solution.</div>

    <svg width="0" height="0" style="position:absolute">
      <defs>
        <radialGradient id="ballShade" cx="35%" cy="35%" r="70%">
          <stop offset="0%" stop-color="#c8344d"/>
          <stop offset="60%" stop-color="#a3182f"/>
          <stop offset="100%" stop-color="#5c0a18"/>
        </radialGradient>
        <symbol id="tickBall" viewBox="0 0 54 40">
          <circle cx="20" cy="20" r="18" fill="url(#ballShade)"/>
          <path d="M12 26 L52 4" stroke="#111" stroke-width="2.5" stroke-linecap="round"/>
        </symbol>
      </defs>
    </svg>
    <svg class="tick-ball" style="left:28px;top:626px"><use href="#tickBall"/></svg>
    <svg class="tick-ball" style="left:73px;top:669px"><use href="#tickBall"/></svg>
    <svg class="tick-ball" style="left:104px;top:719px"><use href="#tickBall"/></svg>
    <svg class="tick-ball" style="left:689px;top:764px"><use href="#tickBall"/></svg>
    <svg class="tick-ball" style="left:740px;top:813px"><use href="#tickBall"/></svg>
    <svg class="tick-ball" style="left:683px;top:858px"><use href="#tickBall"/></svg>

    <div class="price-badge">
      <span class="price-label">Low cost structure</span>
      <span class="price-amount">$350</span>
      <span class="price-period">per month</span>
      <span class="price-no">NO</span>
      <span class="price-fees">Transaction fees</span>
    </div>

    <div class="call">
      <svg width="18" height="46" viewBox="0 0 18 46" aria-hidden="true">
        <path d="M14 1 C6 2 1 10 1 23 C1 36 6 44 14 45 L17 44 L17 33 L11 32 C9 28 9 18 11 14 L17 13 L17 2 Z" fill="var(--brand-red)"/>
      </svg>
      <span>CALL NOW : (555) 482-9167 ext. 204</span>
    </div>
  </main>
</body>
</html>
```